Harborline Crest Insurance Services

we are a high end insurance agency we specialize on Auto | Home | Business | Life looking for something professional and luxuries at the same time. if you guys need anything else please let me know.

Auto | Home | Business | Life must be under logo on the back with black background.

i want the back part to be black with our gold logo on it.

Target Market(s)

Auto | Home | Business | Life

Industry/Entity Type

Insurance Broker

Contact Information for Business Card

My logo is gold so a black in the back would be nice.

Font styles to use
Serif

Colors
000000

Requirements
Must have
• Big logo on the back with black background.

```html
<!DOCTYPE html>
<html lang="en">
<head>
<meta charset="utf-8">
<title>Harborline Crest Insurance Services — Business Card</title>
<link rel="stylesheet" href="https://fonts.googleapis.com/css2?family=Cinzel:wght@600&family=Arimo:wght@400&display=swap">
<style>
  :root {
    --backdrop: #2b2b2b;
    --card: #050505;
    --gold: #f2b714;
    --gold-line: #c99a12;
    --silver: #9a9a9a;
    --white: #f2f2f2;
  }
  * { margin: 0; padding: 0; box-sizing: border-box; }
  html, body { width: 1200px; height: 900px; overflow: hidden; background: var(--backdrop); }
  .canvas { position: relative; width: 1200px; height: 900px; }

  .card {
    position: absolute;
    width: 640px; height: 366px;
    background: var(--card);
    box-shadow: 0 18px 40px rgba(0,0,0,.55);
    overflow: hidden;
  }
  .card--brand { left: 70px; top: 60px; }
  .card--contact { left: 490px; top: 474px; }

  .wordmark { display: flex; align-items: center; gap: 12px; }
  .wordmark__dot { width: 14px; height: 14px; border-radius: 50%; background: var(--gold); flex: none; }
  .wordmark__name {
    font-family: "Cinzel", Georgia, serif; font-weight: 600;
    color: var(--gold); letter-spacing: .5px; line-height: 1;
  }
  .wordmark__sub {
    font-family: "Arimo", Arial, sans-serif; color: var(--silver);
    letter-spacing: 4px; text-transform: uppercase;
  }

  /* brand side */
  .card--brand .lockup { position: absolute; left: 150px; top: 220px; }
  .card--brand .wordmark__name { font-size: 28px; }
  .card--brand .wordmark__sub { font-size: 12px; margin: 6px 0 0 26px; }
  .services {
    margin: 8px 0 0 26px;
    font-family: "Arimo", Arial, sans-serif; font-size: 13px;
    color: var(--gold); letter-spacing: .5px;
  }
  .services .sep { color: var(--white); margin: 0 5px; }
  .rule { position: absolute; left: 470px; top: 196px; width: 170px; height: 1px; background: var(--gold-line); }

  /* contact side */
  .card--contact .lockup { position: absolute; left: 230px; top: 62px; }
  .card--contact .wordmark__name { font-size: 24px; }
  .card--contact .wordmark__sub { font-size: 10px; margin: 5px 0 0 26px; }

  .contact {
    position: absolute; right: 40px; top: 150px;
    font-family: "Arimo", Arial, sans-serif; font-size: 14px;
    color: var(--white); text-align: right; list-style: none; line-height: 1.45;
  }
  .contact li { display: flex; justify-content: flex-end; align-items: center; gap: 10px; }
  .contact .muted { color: var(--silver); }
  .contact svg { width: 12px; height: 12px; fill: none; stroke: var(--gold); stroke-width: 2; }
  .contact .gap { margin-top: 6px; }

  .person { position: absolute; left: 44px; bottom: 42px; }
  .person__name {
    font-family: "Cinzel", Georgia, serif; font-weight: 600;
    font-size: 20px; color: var(--gold); letter-spacing: .5px;
  }
  .person__role { font-family: "Arimo", Arial, sans-serif; font-size: 15px; color: var(--silver); margin-top: 2px; }
</style>
</head>
<body>
<main class="canvas">

  <section class="card card--brand">
    <div class="lockup">
      <div class="wordmark">
        <span class="wordmark__dot"></span>
        <span class="wordmark__name">Harborline Crest</span>
      </div>
      <div class="wordmark__sub">Insurance Services</div>
      <div class="services">AUTO<span class="sep">|</span>HOME<span class="sep">|</span>BUSINESS<span class="sep">|</span>LIFE</div>
    </div>
    <div class="rule"></div>
  </section>

  <section class="card card--contact">
    <div class="lockup">
      <div class="wordmark">
        <span class="wordmark__dot"></span>
        <span class="wordmark__name">Harborline Crest</span>
      </div>
      <div class="wordmark__sub">Insurance Services</div>
    </div>

    <ul class="contact">
      <li class="muted">240 Harbor View Ave</li>
      <li class="muted">Larkmoor, CA 92250</li>
      <li class="gap">+1 555-014-2270
        <svg viewBox="0 0 24 24"><path d="M5 3l4 1 1 5-2 2a12 12 0 0 0 5 5l2-2 5 1 1 4-3 2C10 21 3 14 3 6z"/></svg>
      </li>
      <li>info@harborlinecrest.com
        <svg viewBox="0 0 24 24"><rect x="3" y="6" width="18" height="12"/><path d="M3 6l9 7 9-7"/></svg>
      </li>
      <li>www.harborlinecrest.com
        <svg viewBox="0 0 24 24"><circle cx="12" cy="12" r="9"/><path d="M3 12h18M12 3c3 3 3 15 0 18M12 3c-3 3-3 15 0 18"/></svg>
      </li>
    </ul>

    <div class="person">
      <div class="person__name">MARISOL ARDENNE</div>
      <div class="person__role">Managing Director</div>
    </div>
  </section>

</main>
</body>
</html>
```